Hip Hop artist album cover design "Beneath the Copper Lanterns"

We need a CD Cover design for hip hop artist T.V.M.'s new EP "Beneath the Copper Lanterns".

The Final design should communicate the journey from a tough/desparate situation to inner peace and happiness. For example, a dark earth vs a peaceful sky.

Half of the music is dark & sad, the other is hopeful & calm.

The color schemes for past projects have been black, white, grey and green.

Text for cover
Artists: T.V.M. & Dovo
Album Title: Beneath the Copper Lanterns

Target Market(s)

underground hip hop fans

Font styles to use
Sans Serif
Decorative

Requirements
Must have
• Text for cover
• Artists: T.V.M. & Dovo
• Album Title: Beneath the Copper Lanterns
Nice to have
• suggestion: Black and white cover with taints of dark green

```html
<!DOCTYPE html>
<html lang="en">
<head>
<meta charset="utf-8">
<title>Beneath the Copper Lanterns – CD Cover Layout</title>
<link rel="stylesheet" href="https://fonts.googleapis.com/css2?family=Archivo+Black&family=Pinyon+Script&family=Cinzel:wght@400;600&family=Tinos&family=Arimo:wght@400;700&display=swap">
<style>
  :root{
    --navy:#0f1a8c;
    --ink:#111111;
    --red:#e8141b;
    --white:#ffffff;
    --green:#7ee03a;
    --frame-blue:#1a2fb8;
    --line-blue:#5a6de0;
    --note-green:#1f9a3a;
    --table-red:#e5544a;
    --label-orange:#e8541c;
    --label-blue:#3b55d6;
    --script-blue:#1c1f9e;
    --studio-red:#e8141b;
    --mark-grey:#4a4a4a;
  }
  *{box-sizing:border-box;margin:0;padding:0}
  html,body{width:1200px;height:909px;overflow:hidden;background:var(--white)}
  .sheet{position:relative;width:1200px;height:909px;background:var(--white)}

  /* ---------- artwork panels ---------- */
  .front-cover,.back-cover{position:absolute;left:29px;width:400px;height:400px;overflow:hidden}
  .front-cover{top:22px}
  .back-cover{top:445px}
  .disc{position:absolute;width:362px;height:362px;border-radius:50%;overflow:hidden}
  .disc--front{left:461px;top:59px}
  .disc--back{left:462px;top:481px}
  .disc__hole{position:absolute;left:155px;top:155px;width:53px;height:53px;border-radius:50%;background:var(--white)}

  .scene{position:absolute;inset:0}
  .scene--dawn{background:
      radial-gradient(ellipse at 55% 45%,rgba(255,255,250,.95) 0%,rgba(255,255,245,.6) 22%,rgba(255,255,255,0) 48%),
      linear-gradient(180deg,#b9cfc5 0%,#d9e6de 20%,#e9efe6 45%,#c8ccc2 64%,#8d918c 74%,#5b5d5a 86%,#3a3b39 100%);}
  .scene--dusk{background:linear-gradient(180deg,#0d0d0d 0%,#2b2b2b 22%,#6e6e6e 46%,#b4b4b4 62%,#8c8c8c 72%,#4a4a4a 86%,#262626 100%)}

  /* ---------- front title type ---------- */
  .title-bold{font-family:"Archivo Black",sans-serif;color:var(--navy);line-height:1;display:block}
  .title-script{font-family:"Pinyon Script",cursive;color:var(--ink);line-height:1;display:block}
  .front-title{position:absolute;left:0;top:66px;width:100%;text-align:center;font-weight:400}
  .front-title .title-bold{font-size:33px}
  .front-title .copper{font-size:78px;margin-top:6px}
  .front-title .lanterns{font-size:60px;margin-top:4px;padding-left:60px}

  .disc-title{position:absolute;left:0;top:22px;width:100%;text-align:center;font-weight:400}
  .disc-title .title-bold{font-size:24px}
  .disc-title .copper{font-size:52px;margin-top:2px}
  .disc-title .lanterns{font-size:40px;padding-left:44px}

  /* ---------- format checklist ---------- */
  .formats{position:absolute;font-family:"Archivo Black",sans-serif;color:var(--red);line-height:1}
  .formats li{list-style:none;display:flex;align-items:center}
  .formats .box{background:var(--white);border:1px solid #ddd;margin-right:8px;position:relative}
  .formats--cover{left:296px;top:286px;font-size:11px}
  .formats--cover li{height:17px}
  .formats--cover .box{width:28px;height:15px}
  .formats--disc{left:250px;top:214px;font-size:9px}
  .formats--disc li{height:13px}
  .formats--disc .box{width:22px;height:12px;margin-right:6px}
  .formats .box svg{position:absolute;left:1px;top:-3px}

  /* ---------- artist banner ---------- */
  .banner{position:absolute}
  .banner--cover{left:22px;top:345px}
  .banner--disc{left:38px;top:262px}
  .artists{font-family:"Archivo Black",sans-serif;white-space:nowrap;line-height:1}
  .artists .lead{color:var(--red)}
  .artists .rest{color:var(--white)}
  .banner__text{position:absolute;left:0;top:0;width:100%;display:flex;align-items:center}
  .banner--cover .banner__text{height:46px;padding-left:28px;font-size:29px;letter-spacing:1px}
  .banner--disc .banner__text{height:32px;padding-left:22px;font-size:21px;letter-spacing:1px}

  /* ---------- back side ---------- */
  .back-artists{position:absolute;left:0;width:100%;text-align:center;color:var(--white);font-family:"Archivo Black",sans-serif;line-height:1;font-weight:400}
  .back-cover .back-artists{top:42px;font-size:38px}
  .disc--back .back-artists{top:68px;font-size:27px}

  .back-title{position:absolute;left:0;width:100%;text-align:center;line-height:1}
  .back-title .script{font-family:"Pinyon Script",cursive;color:var(--script-blue);display:block}
  .back-title .caps{font-family:"Cinzel",serif;color:var(--ink);font-weight:400;display:block;letter-spacing:1px}
  .back-title .rule{display:block;margin:0 auto;background:var(--ink)}
  .back-cover .back-title{top:140px}
  .back-cover .back-title .script{font-size:42px;margin-bottom:4px}
  .back-cover .back-title .caps{font-size:34px}
  .back-cover .back-title .rule{width:300px;height:3px;margin:14px auto 16px}
  .disc--back .back-title{top:216px}
  .disc--back .back-title .script{font-size:26px;margin-bottom:2px}
  .disc--back .back-title .caps{font-size:22px}
  .disc--back .back-title .rule{width:180px;height:2px;margin:8px auto 9px}

  .cd-mark{position:absolute;display:flex;align-items:center;font-family:"Archivo Black",sans-serif;color:var(--green);line-height:1}
  .back-cover .cd-mark{left:275px;top:358px;font-size:26px;gap:10px}
  .disc--back .cd-mark{left:262px;top:300px;font-size:14px;gap:4px}

  /* ---------- title block ---------- */
  .notes{position:absolute;left:853px;top:38px;width:317px;height:74px;border:5px solid var(--frame-blue);display:flex;align-items:center;justify-content:center;font-family:"Tinos",serif;font-size:22px;color:var(--note-green)}
  .revisions-rule{position:absolute;left:853px;top:127px;width:324px;height:1px;background:#555}
  .revisions-heading{position:absolute;left:853px;top:132px;width:324px;text-align:center;font-family:"Tinos",serif;font-size:17px;color:var(--note-green)}
  .revisions{position:absolute;left:853px;top:160px;width:324px;border-collapse:collapse;font-family:"Arimo",sans-serif;font-size:16px;color:var(--table-red)}
  .revisions th,.revisions td{border:1px solid var(--table-red);height:40px;font-weight:400;text-align:center}
  .revisions th{height:38px}
  .revisions .col-no{width:52px}
  .revisions .col-date{width:78px}

  .info-box{position:absolute;left:853px;width:308px;border:1px solid var(--line-blue)}
  .client{top:419px;height:89px;padding:8px 11px;font-family:"Tinos",serif;font-size:17px;color:var(--label-orange);line-height:1.2}
  .client p+p{margin-top:10px}

  .studio{position:absolute;left:853px;top:526px;width:308px;height:115px;border:5px solid var(--frame-blue);font-family:"Arimo",sans-serif;color:var(--studio-red)}
  .studio__name{position:absolute;left:17px;top:30px;font-size:13px;line-height:1}
  .studio__details{position:absolute;left:17px;top:47px;font-size:8px;line-height:1.25}
  .studio__mark{position:absolute;right:20px;top:14px;width:80px;height:80px;border-radius:50%;background:var(--mark-grey)}

  .job,.drawing{height:108px;padding:14px 18px;font-family:"Arimo",sans-serif}
  .job{top:663px}
  .drawing{top:786px}
  .info-box .label{font-size:14px;color:var(--label-orange)}
  .info-box .value{font-size:14px;font-weight:700;color:var(--label-blue);margin-top:8px;white-space:nowrap;overflow:hidden}
  .drawing .value{margin-top:20px}
</style>
</head>
<body>
<main class="sheet">

  <!-- Front cover -->
  <section class="front-cover">
    <div class="scene scene--dawn" role="img" aria-label="Photograph of a pale cloudy sky with sunlight over a grey mountain range and faint shadowy figures on the dark ground"></div>
    <h1 class="front-title">
      <span class="title-bold">Beneath the</span>
      <span class="title-script copper">Copper</span>
      <span class="title-script lanterns">Lanterns</span>
    </h1>
    <ul class="formats formats--cover">
      <li><span class="box"><svg width="24" height="16" viewBox="0 0 24 16"><path d="M3 8 L9 13 L22 2" fill="none" stroke="#e8141b" stroke-width="2.5"/></svg></span>CD</li>
      <li><span class="box"></span>VCD</li>
      <li><span class="box"></span>DVD</li>
    </ul>
    <div class="banner banner--cover">
      <svg width="378" height="46" viewBox="0 0 378 46"><polygon points="0,0 378,0 356,23 378,46 0,46" fill="#111"/><polygon points="338,0 378,0 358,23 378,46 338,46 322,23" fill="#e8141b"/></svg>
      <div class="banner__text artists"><span class="lead">T.V.M.</span>&nbsp;<span class="rest">&amp; Dovo</span></div>
    </div>
  </section>

  <!-- Front disc -->
  <section class="disc disc--front">
    <div class="scene scene--dawn" role="img" aria-label="Photograph of a pale cloudy sky over grey mountains with faint shadowy figures raising their arms"></div>
    <h2 class="disc-title">
      <span class="title-bold">Beneath the</span>
      <span class="title-script copper">Copper</span>
      <span class="title-script lanterns">Lanterns</span>
    </h2>
    <div class="disc__hole"></div>
    <ul class="formats formats--disc">
      <li><span class="box"><svg width="20" height="13" viewBox="0 0 24 16"><path d="M3 8 L9 13 L22 2" fill="none" stroke="#e8141b" stroke-width="2.5"/></svg></span>CD</li>
      <li><span class="box"></span>VCD</li>
      <li><span class="box"></span>DVD</li>
    </ul>
    <div class="banner banner--disc">
      <svg width="262" height="32" viewBox="0 0 262 32"><polygon points="0,0 262,0 248,16 262,32 0,32" fill="#111"/><polygon points="234,0 262,0 248,16 262,32 234,32 222,16" fill="#e8141b"/></svg>
      <div class="banner__text artists"><span class="lead">T.V.M.</span>&nbsp;<span class="rest">&amp; Dovo</span></div>
    </div>
  </section>

  <!-- Back cover -->
  <section class="back-cover">
    <div class="scene scene--dusk" role="img" aria-label="Black and white photograph of a dark sky fading to a grey mountain range over scrubland"></div>
    <h2 class="back-artists">T.V.M. &amp; Dovo</h2>
    <div class="back-title">
      <span class="script">Beneath the</span>
      <span class="caps">COPPER</span>
      <span class="rule"></span>
      <span class="caps">LANTERNS</span>
    </div>
    <div class="cd-mark">
      <svg width="40" height="26" viewBox="0 0 40 26"><rect x="1" y="1" width="38" height="24" fill="#fff" stroke="#7ee03a" stroke-width="2"/><path d="M7 13 L16 20 L34 6" fill="none" stroke="#7ee03a" stroke-width="3.5"/></svg>
      CD
    </div>
  </section>

  <!-- Back disc -->
  <section class="disc disc--back">
    <div class="scene scene--dusk" role="img" aria-label="Black and white photograph of a dark sky over a grey mountain range and scrubland"></div>
    <h2 class="back-artists">T.V.M. &amp; Dovo</h2>
    <div class="disc__hole"></div>
    <div class="back-title">
      <span class="script">Beneath the</span>
      <span class="caps">COPPER</span>
      <span class="rule"></span>
      <span class="caps">LANTERNS</span>
    </div>
    <div class="cd-mark">
      <svg width="22" height="14" viewBox="0 0 40 26"><rect x="1" y="1" width="38" height="24" fill="#fff" stroke="#7ee03a" stroke-width="2"/><path d="M7 13 L16 20 L34 6" fill="none" stroke="#7ee03a" stroke-width="4"/></svg>
      CD
    </div>
  </section>

  <!-- Title block -->
  <div class="notes">NOTES</div>
  <div class="revisions-rule"></div>
  <div class="revisions-heading">REVISIONS</div>
  <table class="revisions">
    <thead><tr><th class="col-no">No.</th><th class="col-date">Date</th><th>Revision/Issue</th></tr></thead>
    <tbody>
      <tr><td></td><td></td><td></td></tr>
      <tr><td></td><td></td><td></td></tr>
      <tr><td></td><td></td><td></td></tr>
      <tr><td></td><td></td><td></td></tr>
      <tr><td></td><td></td><td></td></tr>
    </tbody>
  </table>

  <div class="info-box client">
    <p>CLIENT: ....</p>
    <p>CLIENT`S SIGNATURE</p>
  </div>

  <div class="studio">
    <p class="studio__name">Bright Crest Studio</p>
    <p class="studio__details">Cell :&nbsp;&nbsp; 0700 123 456 - NAIROBI<br>Email: hello@brightcrest.example</p>
    <span class="studio__mark"></span>
  </div>

  <div class="info-box job">
    <p class="label">JOB TITLE</p>
    <p class="value">CD COVER DESIGN FOR HIP HOP ARTIS</p>
  </div>

  <div class="info-box drawing">
    <p class="label">DRAWING TITLE</p>
    <p class="value">CD COVER</p>
  </div>

</main>
</body>
</html>
```